A Hair, Beauty and Nails Wholesalers Needs a Business Card Design

We need a business card design for our company which is being passed from parents to daughter, so we wont to re-launch the company with an updated, modern, sophisticated, elegant, chic and fresh look which still incorporates the original colour scheme of Hot Pink, Dark Grey and White. The original logo which is attached can be used on the card but we would like to see some designs with the logo and some without, as we have not yet decided if we want the logo on the card. The name of our company is 'RM's Distributors' and the name of our website is RM's GlowandPolish.example.au. We specialise in supplying a massive range of Hair, Beauty and Nail products to the industry. We are based in QLD, Australia but ship many orders via our website all across Australia.

Industry/Entity Type

Business

```html
<!DOCTYPE html>
<html lang="en">
<head>
<meta charset="utf-8">
<title>RM's Distributors – Business Card</title>
<link href="https://fonts.googleapis.com/css2?family=Ubuntu:wght@400;500&display=swap" rel="stylesheet">
<style>
  :root {
    --hot-pink: #e20a84;
    --dark-grey: #9a9b97;
    --ink: #111111;
    --paper: #ffffff;
    --backdrop: #2a2a2c;
  }
  * { margin: 0; padding: 0; box-sizing: border-box; }
  html, body { width: 1200px; height: 900px; overflow: hidden; }
  body {
    background: var(--backdrop);
    font-family: "Ubuntu", sans-serif;
    position: relative;
  }
  .card {
    position: absolute;
    top: 285px;
    width: 540px;
    height: 330px;
    background: var(--paper);
    overflow: hidden;
  }
  .card--front { left: 40px; }
  .card--back { left: 620px; }

  .front-waves { position: absolute; inset: 0; width: 100%; height: 100%; }

  .brand {
    position: absolute;
    display: flex;
    align-items: center;
    gap: 8px;
    color: var(--hot-pink);
    font-weight: 400;
    white-space: nowrap;
  }
  .brand__dot {
    width: 12px; height: 12px;
    border-radius: 50%;
    background: var(--hot-pink);
    flex: none;
  }
  .card--front .brand { left: 24px; top: 88px; font-size: 18px; }
  .card--back .brand { left: 50%; top: 120px; transform: translateX(-50%); font-size: 26px; }
  .card--back .brand__dot { width: 14px; height: 14px; }

  .person {
    position: absolute;
    left: 150px;
    bottom: 40px;
    color: var(--paper);
  }
  .person__name { font-size: 21px; font-weight: 500; }
  .person__role { font-size: 12px; margin-top: 4px; }

  .contact {
    position: absolute;
    right: 26px;
    top: 32px;
    color: var(--paper);
    font-size: 12.5px;
    font-style: normal;
    line-height: 1.45;
    text-align: right;
  }
  .contact__block + .contact__block { margin-top: 12px; }
  .contact__icons {
    position: absolute;
    right: 26px;
    top: 6px;
    display: flex;
    gap: 8px;
  }
  .contact__icons svg { width: 14px; height: 14px; }

  .tagline {
    position: absolute;
    left: 0; right: 0;
    top: 200px;
    text-align: center;
    color: var(--hot-pink);
    font-size: 15px;
  }
</style>
</head>
<body>

<section class="card card--front" aria-label="Business card front">
  <svg class="front-waves" viewBox="0 0 540 330" aria-hidden="true">
    <path fill="var(--dark-grey)" d="M312,0 C272,120 172,170 122,230 C92,270 82,300 77,330 L540,330 L540,0 Z"/>
    <path fill="var(--paper)" d="M322,0 C282,120 182,170 132,230 C102,270 92,300 87,330 L540,330 L540,0 Z"/>
    <path fill="var(--ink)" d="M326,0 C286,120 186,170 136,230 C106,270 96,300 91,330 L540,330 L540,0 Z"/>
    <path fill="var(--paper)" d="M336,0 C296,120 196,170 146,230 C116,270 106,300 101,330 L540,330 L540,0 Z"/>
    <path fill="var(--hot-pink)" d="M342,0 C302,120 202,170 152,230 C122,270 112,300 107,330 L540,330 L540,0 Z"/>
  </svg>

  <div class="brand"><span class="brand__dot"></span>RM's GlowandPolish</div>

  <div class="contact__icons" aria-hidden="true">
    <svg viewBox="0 0 14 14"><rect x="3.5" y="1" width="7" height="12" rx="1.2" fill="none" stroke="#fff" stroke-width="1.4"/></svg>
    <svg viewBox="0 0 14 14"><rect x="1" y="3" width="12" height="8" fill="none" stroke="#fff" stroke-width="1.4"/><path d="M1,3 L7,8 L13,3" fill="none" stroke="#fff" stroke-width="1.4"/></svg>
    <svg viewBox="0 0 14 14"><circle cx="7" cy="7" r="5.8" fill="none" stroke="#fff" stroke-width="1.4"/><path d="M1.2,7 H12.8 M7,1.2 C4,4 4,10 7,12.8 M7,1.2 C10,4 10,10 7,12.8" fill="none" stroke="#fff" stroke-width="1"/></svg>
  </div>

  <address class="contact">
    <div class="contact__block">
      RM's Distributors<br>
      128 Margaret Lane<br>
      HILLVIEW, QLD, 4000
    </div>
    <div class="contact__block">(07) 5550 0123</div>
    <div class="contact__block">
      admin@glowandpolish.example.au<br>
      www.GlowandPolish.example.au
    </div>
  </address>

  <div class="person">
    <div class="person__name">Danielle Morgan</div>
    <div class="person__role">Manager</div>
  </div>
</section>

<section class="card card--back" aria-label="Business card back">
  <div class="brand"><span class="brand__dot"></span>RM's GlowandPolish</div>
  <p class="tagline">For all your Hair, Beauty &amp; Nail supplies.</p>
</section>

</body>
</html>
```